IT support company needs Banner Ad for the top of their quote layout template

We need a banner Ad for the top of our for quote layout template so it is sent out on all our quotes

The banner size must be 827 x 100 pixels - anything larger than 60 KB can cause upload time issues

We have attached our logo and examples of the quote page to see how it looks in the context of the whole page.

Essential elements of the banner
- Must have our logo but this can be changed to be different colours if it makes the design work better i.e. Tidal Ember could be all in white

Colours
- Can use all of our standard colours - Orange, Black, Grey and White

Images
- As a premium IT support company we deal with people and technology so would like to see both of these Incorporated into the banner i.e. people using technology These images could be watermarked or one colour effect.

Look and Feel
- Professional, friendly, people, technology, premium

Target Market
Small business owners and managers

Industry/Entity Type

It Company

```html
<!DOCTYPE html>
<html lang="en">
<head>
<meta charset="utf-8">
<title>Tidal Ember – Quote Banner</title>
<link rel="stylesheet" href="https://fonts.googleapis.com/css2?family=Orbitron:wght@700;900&family=Michroma&display=swap">
<style>
  :root {
    --stage-grey: #6b6b6b;
    --ink-black: #262626;
    --brand-orange: #ff6200;
    --paper-white: #ffffff;
    --sky-deep: #27a3df;
    --sky-soft: #9fcdef;
    --sky-pale: #e8f3fb;
  }
  html, body {
    margin: 0;
    padding: 0;
    width: 1200px;
    height: 1200px;
    overflow: hidden;
    background: var(--stage-grey);
  }
  .banner {
    position: absolute;
    left: 41px;
    top: 534px;
    width: 1117px;
    height: 134px;
    overflow: hidden;
  }
  .banner-shapes {
    position: absolute;
    inset: 0;
    display: block;
  }
  .headline {
    position: absolute;
    left: 51px;
    top: 27px;
    margin: 0;
    font-family: "Orbitron", sans-serif;
    font-weight: 900;
    font-size: 27px;
    line-height: 31px;
    letter-spacing: 0.3px;
    color: var(--brand-orange);
    text-transform: uppercase;
  }
  .tagline {
    position: absolute;
    left: 51px;
    top: 91px;
    margin: 0;
    font-family: "Michroma", sans-serif;
    font-size: 14px;
    line-height: 18px;
    color: var(--paper-white);
  }
  .brand-name {
    position: absolute;
    left: 791px;
    width: 326px;
    top: 0;
    height: 134px;
    display: flex;
    align-items: center;
    justify-content: center;
    margin: 0;
    font-family: "Orbitron", sans-serif;
    font-weight: 700;
    font-size: 29px;
    color: var(--paper-white);
    text-transform: uppercase;
    padding-top: 8px;
    box-sizing: border-box;
  }
</style>
</head>
<body>
  <div class="banner">
    <svg class="banner-shapes" width="1117" height="134" viewBox="0 0 1117 134" xmlns="http://www.w3.org/2000/svg">
      <defs>
        <linearGradient id="sky-fill" x1="0" y1="0.3" x2="1" y2="0.6">
          <stop offset="0" stop-color="var(--sky-deep)"/>
          <stop offset="0.55" stop-color="var(--sky-soft)"/>
          <stop offset="1" stop-color="var(--sky-pale)"/>
        </linearGradient>
      </defs>
      <rect class="dark-panel" x="0" y="0" width="1117" height="134" fill="var(--ink-black)"/>
      <path class="orange-sweep" d="M379 134 C382 70 400 28 430 0 L1117 0 L1117 134 Z" fill="var(--brand-orange)"/>
      <path class="white-sweep" d="M396 134 C398 72 414 28 438 0 L1117 0 L1117 134 Z" fill="var(--paper-white)"/>
      <g role="img" aria-label="Image area: people working with technology, shown in a light blue one-colour treatment">
        <path class="image-area" d="M416 134 C409 72 420 26 446 0 L791 0 L791 134 Z" fill="url(#sky-fill)"/>
      </g>
      <rect class="brand-panel" x="791" y="0" width="326" height="134" fill="var(--brand-orange)"/>
    </svg>

    <h1 class="headline">Lorem Ipsum<br>Dolor Sit Amet</h1>
    <p class="tagline">consectetuer adipiscing elit</p>
    <p class="brand-name">Tidal Ember</p>
  </div>
</body>
</html>
```